Business card for real estate agent / office

We're looking for a new business card. We want something that is pretty clean, modern and sleek. Something that also tells people that we are a new age company...cutting edge. Although real estate has been done a certain way the last 100 years, we have energy and vibrance. Company name is Silver Meadow Properties. info can be found here: http://www.smprealtyhub.example/

needs to include: Name, title, phone number, email. our license number also needs to be displayed somewhere.

Target Market(s)

25-55 homeowners or potential homeowners

Industry/Entity Type

Business

Contact Information for Business Card

we need business card designs for real estate agent / office

Font styles to use
Serif

Requirements
Must have
• needs to include: Name, title, phone number, email. our license number also needs to be displayed somewhere and company name.
Nice to have
• placement area for photo

```html
<!DOCTYPE html>
<html lang="en">
<head>
<meta charset="utf-8">
<title>Silver Meadow Properties – Mini Brand Guide</title>
<link href="https://fonts.googleapis.com/css2?family=Montserrat:wght@600&family=Open+Sans:wght@400;600&family=Ubuntu:wght@500&display=swap" rel="stylesheet">
<style>
:root{
  --navy:#154c70;
  --green:#5fb33d;
  --white:#ffffff;
  --ink:#1f2d3a;
  --paper-shadow:0 6px 18px rgba(0,0,0,.12);
}
*{box-sizing:border-box;margin:0;padding:0}
html,body{width:1200px;height:1200px;overflow:hidden;background:var(--white)}
body{position:relative;font-family:"Open Sans",sans-serif;color:var(--ink)}
.abs{position:absolute}
.corner-triangle{left:1016px;top:0;width:184px;height:172px;background:var(--navy);clip-path:polygon(0 0,100% 0,100% 100%)}

/* brand wordmark */
.brand{position:absolute;display:flex;flex-direction:column;align-items:center;font-family:"Ubuntu",sans-serif;font-weight:500;line-height:1;color:var(--navy);text-align:center}
.brand .mark{width:.9em;height:.9em;background:currentColor;margin-bottom:.3em}
.brand .name{white-space:nowrap}
.brand .sub{font-size:.42em;letter-spacing:.18em;margin-top:.2em}
.brand.on-dark{color:var(--white)}

.header-brand{left:112px;top:52px;font-size:19px}
.header-divider{left:252px;top:50px;width:3px;height:80px;background:var(--green)}
.guide-banner{left:269px;top:59px;width:197px;height:63px;background:var(--navy);clip-path:polygon(0 0,100% 0,84% 100%,0 100%);color:var(--white);font-size:14px;line-height:63px;padding-left:14px}

.card{position:absolute;width:275px;height:154px;background:var(--white);box-shadow:var(--paper-shadow);overflow:hidden}
.card.navy{background:var(--navy)}
.card.green{background:var(--green)}
.card .brand.center{left:0;right:0;top:44px;font-size:21px}

.agent-name{position:absolute;font-family:"Montserrat",sans-serif;font-weight:600;color:var(--navy);font-size:11.5px;letter-spacing:.02em}
.agent-title{position:absolute;font-size:4.8px;color:var(--green);letter-spacing:.02em}
.license-bar{position:absolute;background:var(--navy);color:var(--white);font-size:7.5px;display:flex;align-items:center;justify-content:center}
.contacts{position:absolute;list-style:none;color:var(--green)}
.contacts li{display:flex;align-items:center;white-space:nowrap}
.contacts .icon{flex:none;border-radius:50%;background:var(--green);display:flex;align-items:center;justify-content:center;color:var(--white)}
.contacts.light{color:var(--white)}
.contacts.light .icon{background:var(--white);color:var(--green)}
.contacts.small{font-size:5.5px}
.contacts.small li{height:13px}
.contacts.small .icon{width:8px;height:8px;margin-right:5px}
.contacts.small .icon svg{width:5px;height:5px}
.green-tab{position:absolute;background:var(--green)}
.navy-band{position:absolute;background:var(--navy)}

.color-block{left:122px;top:579px;width:275px;height:87px;display:flex;font-size:17px;letter-spacing:.3em;color:var(--white)}
.color-block span{flex:1;display:flex;align-items:center;justify-content:center}
.color-block .navy{background:var(--navy)}
.color-block .green{background:var(--green)}
.swatch-title{left:434px;top:577px;font-size:10px;letter-spacing:.25em}
.swatch{position:absolute;left:434px;width:28px;height:28px}
.swatch-code{position:absolute;left:473px;font-size:7px;letter-spacing:.3em;line-height:9px}
.swatch-rule{left:702px;width:6px}

.letterhead{position:absolute;left:746px;top:198px;width:331px;height:468px;background:var(--white);box-shadow:var(--paper-shadow);overflow:hidden}
.envelope{position:absolute;left:122px;top:704px;width:955px;height:414px;background:var(--white);box-shadow:var(--paper-shadow);overflow:hidden}
.contacts.large{font-size:14px}
.contacts.large li{height:28px}
.contacts.large .icon{width:21px;height:21px;margin-right:9px}
.contacts.large .icon svg{width:12px;height:12px}
</style>
</head>
<body>
<svg width="0" height="0" style="position:absolute" aria-hidden="true">
  <symbol id="i-web" viewBox="0 0 10 10"><rect x="1" y="1" width="3.4" height="3.4" fill="currentColor"/><rect x="5.6" y="1" width="3.4" height="3.4" fill="currentColor"/><rect x="1" y="5.6" width="3.4" height="3.4" fill="currentColor"/><rect x="5.6" y="5.6" width="3.4" height="3.4" fill="currentColor"/></symbol>
  <symbol id="i-mail" viewBox="0 0 10 10"><circle cx="5" cy="5" r="3.8" fill="none" stroke="currentColor" stroke-width="1.2"/><circle cx="5" cy="5" r="1.5" fill="none" stroke="currentColor" stroke-width="1.1"/></symbol>
  <symbol id="i-phone" viewBox="0 0 10 10"><path d="M2.2 1 3.8 1 4.4 3.2 3.3 4.1C3.8 5.2 4.8 6.2 5.9 6.7L6.8 5.6 9 6.2 9 7.8C9 8.5 8.4 9 7.7 9 4 8.7 1.3 6 1 2.3 1 1.6 1.5 1 2.2 1Z" fill="currentColor"/></symbol>
</svg>

<div class="abs corner-triangle"></div>

<header>
  <div class="brand header-brand"><span class="mark"></span><span class="name">Silver Meadow</span><span class="sub">PROPERTIES</span></div>
  <div class="abs header-divider"></div>
  <div class="abs guide-banner">MINI BRAND GUIDE</div>
</header>

<!-- card front, white -->
<section class="card" style="left:122px;top:198px">
  <div class="agent-name" style="left:15px;top:29px">DANIEL REYES</div>
  <div class="agent-title" style="right:137px;top:44px">REAL ESTATE BROKER, REALTOR, MBA</div>
  <div class="license-bar" style="left:0;top:60px;width:138px;height:19px">CA BRE #02957316</div>
  <ul class="contacts small" style="left:51px;top:83px">
    <li><span class="icon"><svg><use href="#i-web"/></svg></span>www.smprealtyhub.example</li>
    <li><span class="icon"><svg><use href="#i-mail"/></svg></span>email@smprealtyhub.example</li>
    <li><span class="icon"><svg><use href="#i-phone"/></svg></span>555 204 7781</li>
  </ul>
  <div class="brand" style="left:158px;top:60px;width:112px;font-size:16px"><span class="mark"></span><span class="name">Silver Meadow</span><span class="sub">PROPERTIES</span></div>
</section>

<!-- card back, navy -->
<section class="card navy" style="left:434px;top:198px">
  <div class="brand on-dark center"><span class="mark"></span><span class="name">Silver Meadow</span><span class="sub">PROPERTIES</span></div>
</section>

<!-- card back, green -->
<section class="card green" style="left:122px;top:389px">
  <div class="brand on-dark center"><span class="mark"></span><span class="name">Silver Meadow</span><span class="sub">PROPERTIES</span></div>
</section>

<!-- card front, alternate -->
<section class="card" style="left:434px;top:389px">
  <div class="brand" style="left:22px;top:20px;width:100px;font-size:14px"><span class="mark"></span><span class="name">Silver Meadow</span><span class="sub">PROPERTIES</span></div>
  <div class="agent-name" style="right:12px;top:66px">DANIEL REYES</div>
  <div class="agent-title" style="right:13px;top:81px">REAL ESTATE BROKER, REALTOR, MBA</div>
  <div class="navy-band license-bar" style="left:118px;top:97px;width:157px;height:26px;padding-left:24px">CA BRE #02957316</div>
  <div class="green-tab" style="left:0;top:89px;width:137px;height:42px;clip-path:polygon(0 0,100% 0,85% 100%,0 100%)"></div>
  <ul class="contacts small light" style="left:14px;top:90px">
    <li><span class="icon"><svg><use href="#i-web"/></svg></span>www.smprealtyhub.example</li>
    <li><span class="icon"><svg><use href="#i-mail"/></svg></span>email@smprealtyhub.example</li>
    <li><span class="icon"><svg><use href="#i-phone"/></svg></span>555 204 7781</li>
  </ul>
</section>

<!-- colour guide -->
<div class="abs color-block"><span class="navy">COLOR</span><span class="green">GUIDE</span></div>
<div class="abs swatch-title">COLOR GUIDE</div>
<div class="swatch" style="top:602px;background:var(--navy)"></div>
<div class="swatch-code" style="top:607px">RG B HEX:#033D03<br>CMYK HEX:#273D2C</div>
<div class="swatch" style="top:639px;background:var(--green)"></div>
<div class="swatch-code" style="top:644px">RG B HEX:#72A632<br>CMYK HEX:#71A63B</div>
<div class="abs swatch-rule" style="top:579px;height:44px;background:var(--navy)"></div>
<div class="abs swatch-rule" style="top:623px;height:43px;background:var(--green)"></div>

<!-- letterhead -->
<section class="letterhead">
  <div class="brand" style="left:0;right:0;top:12px;font-size:13px"><span class="mark"></span><span class="name">Silver Meadow</span><span class="sub">PROPERTIES</span></div>
  <div class="navy-band" style="left:116px;right:0;top:412px;height:28px"></div>
  <div class="green-tab" style="left:0;top:404px;width:137px;height:43px;clip-path:polygon(0 0,100% 0,84% 100%,0 100%)"></div>
  <ul class="contacts small light" style="left:13px;top:406px">
    <li><span class="icon"><svg><use href="#i-web"/></svg></span>www.smprealtyhub.example</li>
    <li><span class="icon"><svg><use href="#i-mail"/></svg></span>email@smprealtyhub.example</li>
    <li><span class="icon"><svg><use href="#i-phone"/></svg></span>555 204 7781</li>
  </ul>
</section>

<!-- envelope -->
<section class="envelope">
  <div class="brand" style="right:40px;top:26px;width:170px;font-size:27px"><span class="mark"></span><span class="name">Silver Meadow</span><span class="sub">PROPERTIES</span></div>
  <div class="navy-band" style="left:258px;right:0;top:306px;height:50px"></div>
  <div class="green-tab" style="left:0;top:290px;width:300px;height:96px;clip-path:polygon(0 0,100% 0,83% 100%,0 100%)"></div>
  <ul class="contacts large light" style="left:29px;top:296px">
    <li><span class="icon"><svg><use href="#i-web"/></svg></span>www.smprealtyhub.example</li>
    <li><span class="icon"><svg><use href="#i-mail"/></svg></span>email@smprealtyhub.example</li>
    <li><span class="icon"><svg><use href="#i-phone"/></svg></span>555 204 7781</li>
  </ul>
</section>
</body>
</html>
```